Business Card Design For Office Furniture Clearance Company

Kestrel Office Clearance - our company name pretty much explains what we do, we clear offices for high end clients, mainly plc's and large international companies.

We require a nice looking business card that displays professionalism but without being too serious.

It would be nice to see just a little more than a conventional boring business card, make sure you add some flare.

Industry/Entity Type

Office Furniture

Contact Information for Business Card

CARD 1

Tom Pardew
Director
tom@kestrelofficeclearance.co.uk
m: 07700 513928

t: 01632 419063
www.kestrelofficeclearance.co.uk

Kestrel Office Clearance
Unit K4 B
3-7 Ferndale Lane
Bletchley
Milton Keynes
ZZ9 4QX

free office clearances… you cant get better than that.

CARD 2

Henry Walbrook
Director
henry@kestrelofficeclearance.co.uk
m: 07700 628157

t: 01632 419063

Kestrel Office Clearance
Unit K4 B
3-7 Ferndale Lane
Bletchley
Milton Keynes
ZZ9 4QX

Font styles to use
Sans Serif

Requirements
Must have
• A white background - as we have a blue logo.
Nice to have
• Nice use of the logo - play around with this and dissect it.

```html
<!DOCTYPE html>
<html lang="en">
<head>
<meta charset="utf-8">
<title>Kestrel Office Clearance – Business Cards</title>
<link rel="stylesheet" href="https://fonts.googleapis.com/css2?family=Open+Sans:wght@400;600;700&display=swap">
<style>
  :root {
    --page-bg: #e9eaec;
    --card-white: #ffffff;
    --deep-blue: #1c5e91;
    --bright-blue: #1d7bba;
    --text-white: #ffffff;
    --shadow: rgba(0, 0, 0, 0.18);
  }
  * { box-sizing: border-box; margin: 0; padding: 0; }
  html, body {
    width: 1200px;
    height: 1200px;
    overflow: hidden;
    background: var(--page-bg);
    font-family: "Open Sans", Arial, sans-serif;
  }
  .canvas { position: relative; width: 1200px; height: 1200px; }

  .card {
    position: absolute;
    overflow: hidden;
    box-shadow: 0 10px 24px var(--shadow);
  }

  /* Reverse side */
  .card-back {
    left: 100px; top: 160px;
    width: 620px; height: 370px;
    background: var(--deep-blue);
  }
  .card-back .brand-disc {
    position: absolute;
    left: 205px; top: 45px;
    width: 210px; height: 210px;
    border-radius: 50%;
    background: var(--bright-blue);
  }
  .card-back .wordmark {
    position: absolute;
    left: 0; right: 0; top: 272px;
    text-align: center;
    color: var(--text-white);
    font-weight: 700;
    font-size: 20px;
  }
  .card-back .web {
    position: absolute;
    left: 0; right: 0; bottom: 26px;
    text-align: center;
    color: var(--text-white);
    font-size: 15px;
    letter-spacing: 3px;
  }

  /* Front side */
  .card-front {
    left: 460px; top: 700px;
    width: 640px; height: 380px;
    background: var(--card-white);
  }
  .card-front .info-band {
    position: absolute;
    left: 180px; right: 0;
    top: 92px; bottom: 42px;
    background: var(--deep-blue);
  }
  .card-front .brand-disc {
    position: absolute;
    left: 26px; top: 52px;
    width: 296px; height: 296px;
    border-radius: 50%;
    background: var(--bright-blue);
    box-shadow: 6px 6px 14px rgba(0,0,0,0.22);
  }
  .contact {
    position: absolute;
    left: 360px; top: 100px;
    color: var(--text-white);
  }
  .contact .name {
    font-weight: 700;
    font-size: 21px;
    letter-spacing: 0.3px;
    text-transform: uppercase;
  }
  .contact .role { font-size: 13px; margin-top: -2px; }
  .contact .lines { list-style: none; margin-top: 14px; }
  .contact .lines li {
    display: flex; align-items: center;
    font-size: 14px; line-height: 22px;
  }
  .contact .icon {
    width: 15px; height: 15px;
    margin-right: 10px; flex: none;
  }
  .contact .company {
    margin-top: 12px;
    font-weight: 700; font-size: 15px;
  }
  .contact .address { font-size: 14px; line-height: 20px; }
</style>
</head>
<body>
<div class="canvas">

  <section class="card card-back" aria-label="Business card reverse">
    <div class="brand-disc"></div>
    <p class="wordmark">Kestrel Office Clearance</p>
    <p class="web">www.kestrelofficeclearance.co.uk</p>
  </section>

  <section class="card card-front" aria-label="Business card front">
    <div class="info-band"></div>
    <div class="brand-disc"></div>
    <div class="contact">
      <h1 class="name">Tom Pardew</h1>
      <p class="role">Director</p>
      <ul class="lines">
        <li>
          <svg class="icon" viewBox="0 0 16 16" aria-hidden="true"><circle cx="8" cy="8" r="8" fill="#fff"/><rect x="5.3" y="3" width="5.4" height="10" rx="1" fill="none" stroke="#1c5e91" stroke-width="1.4"/></svg>
          07700 513928
        </li>
        <li>
          <svg class="icon" viewBox="0 0 16 16" aria-hidden="true"><circle cx="8" cy="8" r="8" fill="#fff"/><path d="M5 4.2c.6-.5 1.2-.3 1.5.3l.6 1.2c.2.5 0 .9-.4 1.2.5 1.1 1.3 1.9 2.4 2.4.3-.4.7-.6 1.2-.4l1.2.6c.6.3.8.9.3 1.5-.9 1-2.4 1-4-.2-1.3-1-2.3-2-3.2-3.4C3.9 6.1 4 4.9 5 4.2z" fill="#1c5e91"/></svg>
          01632 419063
        </li>
        <li>
          <svg class="icon" viewBox="0 0 16 16" aria-hidden="true"><circle cx="8" cy="8" r="8" fill="#fff"/><rect x="3.8" y="5" width="8.4" height="6" fill="none" stroke="#1c5e91" stroke-width="1.2"/><path d="M3.8 5l4.2 3.4L12.2 5" fill="none" stroke="#1c5e91" stroke-width="1.2"/></svg>
          tom@kestrelofficeclearance.co.uk
        </li>
        <li>
          <svg class="icon" viewBox="0 0 16 16" aria-hidden="true"><circle cx="8" cy="8" r="7" fill="none" stroke="#fff" stroke-width="1.4"/><ellipse cx="8" cy="8" rx="3" ry="7" fill="none" stroke="#fff" stroke-width="1.1"/><path d="M1 8h14M2.5 4.5h11M2.5 11.5h11" stroke="#fff" stroke-width="1"/></svg>
          www.kestrelofficeclearance.co.uk
        </li>
      </ul>
      <p class="company">Kestrel Office Clearance</p>
      <p class="address">Unit K4 B, 3-7 Ferndale Lane<br>Ashgrove, Harlow Vale, ZZ9 4QX</p>
    </div>
  </section>

</div>
</body>
</html>
```